PowerPoint Strategy presentation to be converted to professional looking

Convert the supplied PowerPoint presentation to a professional strategy presentation. Designer must have knowledge of how strategies are presented.

Target Market(s)

Management team

Industry/Entity Type

Finance

Font styles to use
Sans Serif

Colors
0054AA
0677BA
7BADD7
CADEEF
E8F1F8

Requirements
Must have
• Strategy must look professional
Nice to have
• Animations would be welcomed

```html
<!DOCTYPE html>
<html lang="en">
<head>
<meta charset="utf-8">
<title>QHF Transformation Strategy 2026 – ExCom Alignment</title>
<link href="https://fonts.googleapis.com/css2?family=Open+Sans:wght@400;600;700;800&display=swap" rel="stylesheet">
<style>
:root{
  --blue-deep:#003a78;
  --blue:#0054AA;
  --blue-mid:#0677BA;
  --blue-light:#7BADD7;
  --blue-pale:#CADEEF;
  --blue-mist:#E8F1F8;
  --slate:#33475b;
  --grey:#6b6b6b;
  --ink:#262626;
}
*{box-sizing:border-box;margin:0;padding:0}
html,body{width:1200px;height:1200px;overflow:hidden;background:#fff}
body{position:relative;font-family:"Open Sans",Arial,sans-serif;color:var(--ink)}
.slide{position:absolute;width:356px;height:200px;overflow:hidden;background:linear-gradient(160deg,#fff 55%,var(--blue-mist) 82%,#fff 100%);box-shadow:0 3px 9px rgba(0,0,0,.22)}
.c1{left:20px}.c2{left:423px}.c3{left:825px}
.r1{top:42px}.r2{top:271px}.r3{top:500px}.r4{top:729px}.r5{top:958px}
.abs{position:absolute}
.frame{position:absolute;left:25px;top:17px;width:308px;height:160px;border:1px solid var(--blue)}
.title-bar{position:absolute;left:25px;top:6px;width:264px;height:24px;background:linear-gradient(90deg,var(--blue-mid),var(--blue-deep));color:#fff;font-weight:700;font-size:11px;line-height:24px;padding-left:3px;white-space:nowrap}
.foot{position:absolute;left:20px;right:12px;top:183px;height:10px;display:flex;align-items:center;gap:5px;font-size:3.6px;color:var(--blue)}
.foot .rule{flex:1;height:.5px;background:var(--blue)}
.foot .brand{display:flex;align-items:center;gap:2px;font-weight:700;font-size:3.8px}
.foot .brand::before{content:"";width:5px;height:5px;border-radius:50%;background:var(--blue)}
.hl-title{color:var(--blue);font-weight:700;font-size:7px}
.note{font-size:4.1px;line-height:1.25;color:var(--ink)}
.note ul{padding-left:5px}
.note b{font-size:4.4px}
.chart svg{display:block}
svg text{font-family:"Open Sans",Arial,sans-serif}

/* cover */
.cover-red{left:25px;top:40px;width:101px;height:122px;background:linear-gradient(135deg,var(--blue-mid),var(--blue-deep));color:#fff;text-align:center;padding-top:30px}
.cover-red h1{font-size:15px;line-height:1.1;font-weight:700}
.cover-red p{font-size:8px;line-height:1.2;margin-top:2px}
.cover-white{left:126px;top:40px;width:205px;height:122px;border:1.5px solid var(--blue);background:#fff;text-align:center}
.cover-brand{margin-top:17px;display:flex;justify-content:center;align-items:center;gap:4px;color:var(--blue);font-weight:700;font-size:9px}
.cover-brand::before{content:"";width:9px;height:9px;border-radius:50%;background:var(--blue)}
.cover-tag{font-size:4.2px;color:var(--grey);margin-top:6px}
.cover-name{font-size:19px;font-weight:800;margin-top:10px;letter-spacing:-.2px}
.cover-name span{color:var(--blue-mid)}
.cover-year{font-size:13px;font-weight:800;line-height:1}
.center-copy{position:absolute;left:0;right:0;top:186px;text-align:center;font-size:3.6px;color:var(--blue)}

/* agenda */
.agenda{background:var(--blue-mist)}
.agenda-box{left:18px;top:23px;width:129px;height:150px;background:linear-gradient(135deg,var(--blue-deep),var(--blue-mid));color:#fff;font-size:16px;font-weight:700;display:flex;align-items:center;justify-content:center;padding-bottom:28px}
.agenda-list{left:163px;top:68px;list-style:none;font-size:11px;line-height:21.5px}
.agenda-list li span{color:var(--blue-mid);margin-right:4px}

/* divider */
.divider .dot{left:154px;top:40px;width:37px;height:37px;border-radius:50%;background:var(--blue-mid)}
.divider .line-t{left:68px;top:58px;width:220px;height:1px;background:var(--blue)}
.divider .line-b{left:68px;top:131px;width:220px;height:1px;background:#444}
.divider h2{position:absolute;left:0;right:0;top:90px;text-align:center;font-size:13.5px;font-weight:700;color:#444}

/* table */
.comp{left:25px;top:40px;border-collapse:separate;border-spacing:1px;font-size:3.5px;text-align:center}
.comp td,.comp th{height:11px;width:22px;padding:0 1px;line-height:1.05}
.comp th{color:#fff;font-weight:600;background:var(--blue-deep)}
.comp th.lab{width:50px;background:var(--blue)}
.comp th.own{background:var(--blue-mid)}
.comp th.dk{background:var(--slate)}
.comp th.lt{background:var(--blue-light)}
.comp tr:nth-child(even) td{background:var(--blue-pale)}
.comp tr:nth-child(odd) td{background:var(--blue-mist)}
.comp td.neg{color:#c0392b}
.tag{position:absolute;top:158px;height:10px;width:38px;color:#fff;font-size:4px;text-align:center;line-height:10px}

/* statement */
.statement{left:25px;top:17px;width:135px;height:160px;background:linear-gradient(160deg,var(--blue-mid),var(--blue-deep));color:#fff;font-weight:700;font-size:10.5px;line-height:1.2;text-align:center;display:flex;align-items:center;justify-content:center}
.statement-text{left:172px;top:57px;width:122px;font-size:5.6px;line-height:1.25;text-align:justify}
.statement-text p+p{margin-top:6px}

/* state pills */
.col-head{position:absolute;top:38px;font-size:6.8px;font-weight:700;border-bottom:1px solid #aaa;padding:0 12px}
.pill{position:absolute;height:24px;border-radius:12px;color:#fff;font-weight:700;font-size:6px;line-height:1.15;display:flex;align-items:center;padding-left:22px}
.pill.now{left:32px;width:112px;background:linear-gradient(180deg,var(--blue-light),var(--blue-mid))}
.pill.next{left:160px;width:124px;background:linear-gradient(180deg,var(--blue),var(--blue-deep));padding-left:18px;font-size:6.6px}

/* KPI */
.kpi-head{position:absolute;top:45px;height:15px;color:#fff;font-size:6px;font-weight:700;text-align:center;line-height:15px}
.kpi-cols{position:absolute;top:65px;font-size:6px;display:flex}
.kpi-row{position:absolute;height:16px;display:flex;align-items:center}
.chev{height:16px;color:#fff;font-weight:700;font-size:4.8px;line-height:1.05;display:flex;align-items:center;justify-content:center;text-align:center;clip-path:polygon(0 0,86% 0,100% 50%,86% 100%,0 100%,14% 50%)}
.chev.val{color:var(--ink);font-weight:400;font-size:6.5px;margin-left:-3px}
.chev.val.strong{color:#fff}

/* pillars */
.pillar{position:absolute;top:70px;width:55px;height:87px;color:#fff;font-weight:700;font-size:6px;text-align:center;line-height:1.2}
.pillar svg{margin:14px auto 6px;display:block}
.pillar .pl{position:absolute;left:0;right:0;top:44px}

/* pillar 1 */
.card{position:absolute;top:65px;width:61px;height:108px;border:1px solid var(--blue-pale);border-radius:3px;background:#fff;box-shadow:0 1px 3px rgba(0,0,0,.15)}
.card h4{height:24px;background:linear-gradient(180deg,var(--blue-mid),var(--blue));color:#fff;font-size:5.6px;text-align:center;display:flex;align-items:center;justify-content:center;line-height:1.1;border-radius:3px 3px 0 0}
.card ul{font-size:3.2px;color:var(--grey);padding:4px 3px 0 8px;line-height:1.6}
.impact{left:300px;top:5px;width:42px;height:42px;border-radius:50%;background:var(--blue);color:#fff;text-align:center;box-shadow:0 2px 4px rgba(0,0,0,.3);padding-top:7px}
.impact b{display:block;font-size:11px;line-height:1}
.impact span{display:block;font-size:3.6px;line-height:1.05}
</style>
</head>
<body>

<!-- 1 Cover -->
<section class="slide c1 r1">
  <div class="abs cover-red"><h1>ExCom Alignment</h1><p>Transformation Strategy</p></div>
  <div class="abs cover-white">
    <div class="cover-brand">Qimma Home Finance</div>
    <div class="cover-tag">Specialists in Home Financing Solutions</div>
    <div class="cover-name"><span>QHF</span>Transformation</div>
    <div class="cover-year">2026</div>
  </div>
  <div class="center-copy">© Copyright 2023 Qimma Home Finance. All Rights Reserved.</div>
</section>

<!-- 2 Agenda -->
<section class="slide agenda c2 r1">
  <div class="abs agenda-box">AGENDA</div>
  <ol class="abs agenda-list">
    <li><span>1.</span>Current State Evaluation</li>
    <li><span>2.</span>Strategy and Financial Plan</li>
    <li><span>3.</span>Other Initiatives</li>
  </ol>
  <div class="foot"><span>2</span><i class="rule"></i><span>© Copyright 2023 Qimma Home Finance. All Rights Reserved.</span><i class="rule"></i><span class="brand">Qimma Home Finance</span></div>
</section>

<!-- 3 Divider -->
<section class="slide divider c3 r1">
  <i class="abs line-t"></i><i class="abs dot"></i>
  <h2>1.&nbsp; Current State Evaluation</h2>
  <i class="abs line-b"></i>
  <div class="foot"><span>3</span><i class="rule"></i><span>© Copyright 2023 Qimma Home Finance. All Rights Reserved.</span><i class="rule"></i><span class="brand">Qimma Home Finance</span></div>
</section>

<!-- 4 Production -->
<section class="slide c1 r2">
  <div class="frame"></div>
  <div class="title-bar">QHF vs. Market Production and Forecast</div>
  <div class="abs chart" style="left:25px;top:34px">
    <svg width="228" height="145" viewBox="0 0 228 145" font-size="3.6">
      <text x="38" y="6" font-weight="700" font-size="4.4">QHF vs. Market Historical Production</text>
      <text x="160" y="6" font-weight="700" font-size="4.4">Forecast</text>
      <rect x="137" y="1" width="64" height="118" fill="none" stroke="#0054AA" stroke-width=".8"/>
      <g stroke="#e2e2e2" stroke-width=".4">
        <line x1="24" y1="12" x2="200" y2="12"/><line x1="24" y1="32" x2="200" y2="32"/><line x1="24" y1="52" x2="200" y2="52"/><line x1="24" y1="72" x2="200" y2="72"/><line x1="24" y1="92" x2="200" y2="92"/><line x1="24" y1="112" x2="200" y2="112"/>
      </g>
      <g font-weight="700" text-anchor="end"><text x="21" y="13">250,000</text><text x="21" y="33">200,000</text><text x="21" y="53">150,000</text><text x="21" y="73">100,000</text><text x="21" y="93">50,000</text><text x="21" y="113">0</text></g>
      <g font-weight="700"><text x="204" y="13">3,500</text><text x="204" y="27">3,000</text><text x="204" y="42">2,500</text><text x="204" y="56">2,000</text><text x="204" y="70">1,500</text><text x="204" y="84">1,000</text><text x="204" y="98">500</text><text x="204" y="113">0</text></g>
      <g font-weight="700" text-anchor="middle"><text x="35" y="122">2019</text><text x="57" y="122">2020</text><text x="79" y="122">2021</text><text x="101" y="122">2022</text><text x="123" y="122">2023</text><text x="147" y="122">2024</text><text x="168" y="122">2025</text><text x="190" y="122">2026</text></g>
      <polyline points="35,58 57,22 79,32 101,50 123,72 147,64 168,60 190,56" fill="none" stroke="#003a78" stroke-width="1"/>
      <polyline points="35,24 57,44 79,61 101,72 123,63 147,43 168,33 190,23" fill="none" stroke="#0677BA" stroke-width="1"/>
      <g fill="#0677BA"><rect x="27" y="16" width="12" height="5"/><rect x="49" y="37" width="12" height="5"/><rect x="71" y="64" width="12" height="5"/><rect x="93" y="75" width="12" height="5"/><rect x="115" y="55" width="12" height="5"/><rect x="137" y="36" width="12" height="5"/><rect x="158" y="26" width="12" height="5"/><rect x="180" y="15" width="12" height="5"/></g>
      <g fill="#003a78"><rect x="20" y="60" width="17" height="5"/><rect x="48" y="15" width="17" height="5"/><rect x="70" y="25" width="17" height="5"/><rect x="92" y="43" width="17" height="5"/><rect x="114" y="75" width="17" height="5"/><rect x="138" y="67" width="17" height="5"/><rect x="159" y="63" width="17" height="5"/><rect x="181" y="59" width="17" height="5"/></g>
      <g fill="#fff" font-size="3.2" text-anchor="middle"><text x="33" y="20">3,075</text><text x="55" y="41">2,381</text><text x="77" y="68">1,769</text><text x="99" y="79">1,395</text><text x="121" y="59">1,696</text><text x="143" y="40">2,406</text><text x="164" y="30">2,771</text><text x="186" y="19">3,107</text>
        <text x="28.5" y="64">135,779</text><text x="56.5" y="19">225,073</text><text x="78.5" y="29">201,481</text><text x="100.5" y="47">154,392</text><text x="122.5" y="79">100,000</text><text x="146.5" y="71">120,000</text><text x="167.5" y="67">130,000</text><text x="189.5" y="63">140,000</text></g>
      <g fill="#fff" stroke="#555" stroke-width=".3"><rect x="40" y="29" width="9" height="4"/><rect x="62" y="50" width="9" height="4"/><rect x="84" y="84" width="9" height="4"/><rect x="106" y="92" width="9" height="4"/><rect x="112" y="48" width="9" height="4"/><rect x="132" y="29" width="9" height="4"/><rect x="152" y="19" width="9" height="4"/><rect x="175" y="7" width="9" height="4"/></g>
      <g font-size="2.6" text-anchor="middle"><text x="44.5" y="32">2.2%</text><text x="66.5" y="53">1.1%</text><text x="88.5" y="87">0.9%</text><text x="110.5" y="95">0.9%</text><text x="116.5" y="51">1.7%</text><text x="136.5" y="32">2.0%</text><text x="156.5" y="22">2.1%</text><text x="179.5" y="10">2.2%</text></g>
      <rect x="25" y="132" width="34" height="5" fill="#fff" stroke="#555" stroke-width=".3"/><text x="27" y="135.8" font-size="3">QHF Market Share</text>
      <line x1="95" y1="134.5" x2="103" y2="134.5" stroke="#0677BA"/><text x="105" y="135.8">QHF</text>
      <line x1="117" y1="134.5" x2="125" y2="134.5" stroke="#003a78"/><text x="127" y="135.8">Market</text>
    </svg>
  </div>
  <div class="abs" style="left:253px;top:36px;width:78px">
    <div class="hl-title">Key Highlights</div>
    <div class="note" style="margin-top:4px">
      <b>Historical</b>
      <ul><li>Overall mortgage production will continue to decline for the 4th year in a row to c. 100,000 units</li><li>QHF is projected to grow mortgage sales by +22% in 2023 (vs. a market decline of -35%)</li></ul>
      <b>Forecast</b>
      <ul><li>Market production is forecast to reach 150,000 units by 2026 led by growth in off plan and self construction</li><li>QHF is forecast to grow production by 83% over the next 3 years (vs. 50% for the overall market)</li></ul>
    </div>
  </div>
  <div class="foot"><span>4</span><i class="rule"></i><span>© Copyright 2023 Qimma Home Finance. All Rights Reserved.</span><i class="rule"></i><span class="brand">Qimma Home Finance</span></div>
</section>

<!-- 5 HSF share -->
<section class="slide c2 r2">
  <div class="frame"></div>
  <div class="title-bar">Market Production Mix – HSF Share</div>
  <div class="abs chart" style="left:25px;top:34px">
    <svg width="212" height="145" viewBox="0 0 212 145" font-size="3.6">
      <text x="80" y="6" font-weight="700" font-size="4.4">HSF vs. Non HSF Share</text>
      <g stroke="#e2e2e2" stroke-width=".4"><line x1="15" y1="8" x2="205" y2="8"/><line x1="15" y1="31" x2="205" y2="31"/><line x1="15" y1="54" x2="205" y2="54"/><line x1="15" y1="77" x2="205" y2="77"/><line x1="15" y1="100" x2="205" y2="100"/><line x1="15" y1="112" x2="205" y2="112"/><line x1="55" y1="8" x2="55" y2="112"/><line x1="95" y1="8" x2="95" y2="112"/><line x1="135" y1="8" x2="135" y2="112"/><line x1="175" y1="8" x2="175" y2="112"/></g>
      <g text-anchor="end"><text x="11" y="9">90%</text><text x="11" y="20.5">80%</text><text x="11" y="32">70%</text><text x="11" y="43.5">60%</text><text x="11" y="55">50%</text><text x="11" y="66.5">40%</text><text x="11" y="78">30%</text><text x="11" y="89.5">20%</text><text x="11" y="101">10%</text><text x="11" y="113">0%</text></g>
      <g text-anchor="middle"><text x="35" y="122">2019</text><text x="75" y="122">2020</text><text x="115" y="122">2021</text><text x="155" y="122">2022</text><text x="195" y="122">2023</text></g>
      <polyline points="35,20.7 75,27.6 115,32.3 155,34.6 195,38" fill="none" stroke="#0677BA" stroke-width="1"/>
      <polyline points="35,87.7 75,80.8 115,76.2 155,73.9 195,70.4" fill="none" stroke="#003a78" stroke-width="1"/>
      <g fill="#0677BA"><rect x="29" y="22" width="10" height="5"/><rect x="69" y="29" width="10" height="5"/><rect x="109" y="26" width="10" height="5"/><rect x="149" y="28" width="10" height="5"/><rect x="189" y="31" width="10" height="5"/></g>
      <g fill="#003a78"><rect x="29" y="80" width="10" height="5"/><rect x="69" y="73" width="10" height="5"/><rect x="109" y="69" width="10" height="5"/><rect x="149" y="66" width="10" height="5"/><rect x="189" y="62" width="10" height="5"/></g>
      <g fill="#fff" text-anchor="middle" font-size="3.3"><text x="34" y="26">79%</text><text x="74" y="33">73%</text><text x="114" y="30">69%</text><text x="154" y="32">67%</text><text x="194" y="35">64%</text><text x="34" y="84">21%</text><text x="74" y="77">27%</text><text x="114" y="73">31%</text><text x="154" y="70">33%</text><text x="194" y="66">36%</text></g>
      <line x1="82" y1="134" x2="90" y2="134" stroke="#003a78"/><text x="91" y="135.3" font-weight="700">HSF</text>
      <line x1="105" y1="134" x2="113" y2="134" stroke="#0677BA"/><text x="114" y="135.3" font-weight="700">Non HSF</text>
    </svg>
  </div>
  <div class="abs" style="left:255px;top:60px;width:72px">
    <div class="hl-title">Key Highlights</div>
    <div class="note" style="margin-top:8px"><ul><li>Non HSF share has increased the last four years and now represents 36% of the overall mortgage market due to decline in HSF sales</li></ul></div>
  </div>
  <div class="foot"><span>5</span><i class="rule"></i><span>© Copyright 2023 Qimma Home Finance. All Rights Reserved.</span><i class="rule"></i><span class="brand">Qimma Home Finance</span></div>
</section>

<!-- 6 HSF products -->
<section class="slide c3 r2">
  <div class="frame"></div>
  <div class="title-bar">Market Production Mix – HSF Products</div>
  <div class="abs chart" style="left:25px;top:34px">
    <svg width="212" height="145" viewBox="0 0 212 145" font-size="3.6">
      <text x="78" y="6" font-weight="700" font-size="4.4">HSF Product Breakdown</text>
      <g stroke="#e2e2e2" stroke-width=".4"><line x1="15" y1="8" x2="205" y2="8"/><line x1="15" y1="34" x2="205" y2="34"/><line x1="15" y1="60" x2="205" y2="60"/><line x1="15" y1="86" x2="205" y2="86"/><line x1="15" y1="112" x2="205" y2="112"/><line x1="55" y1="8" x2="55" y2="112"/><line x1="95" y1="8" x2="95" y2="112"/><line x1="135" y1="8" x2="135" y2="112"/><line x1="175" y1="8" x2="175" y2="112"/></g>
      <g text-anchor="end"><text x="11" y="9">80%</text><text x="11" y="22">70%</text><text x="11" y="35">60%</text><text x="11" y="48">50%</text><text x="11" y="61">40%</text><text x="11" y="74">30%</text><text x="11" y="87">20%</text><text x="11" y="100">10%</text><text x="11" y="113">0%</text></g>
      <g text-anchor="middle"><text x="35" y="122">2019</text><text x="75" y="122">2020</text><text x="115" y="122">2021</text><text x="155" y="122">2022</text><text x="195" y="122">2023</text></g>
      <polyline points="35,30 75,49.6 115,47 155,34 195,22.3" fill="none" stroke="#0677BA" stroke-width="1"/>
      <polyline points="35,73 75,57.4 115,62.6 155,74.3 195,88.6" fill="none" stroke="#003a78" stroke-width="1"/>
      <polyline points="35,102.9 75,99 115,96.4 155,97.7 195,95.1" fill="none" stroke="#7BADD7" stroke-width="1"/>
      <g fill="#0677BA"><rect x="29" y="22" width="10" height="5"/><rect x="69" y="41" width="10" height="5"/><rect x="109" y="39" width="10" height="5"/><rect x="149" y="26" width="10" height="5"/><rect x="189" y="14" width="10" height="5"/></g>
      <g fill="#5f97c8"><rect x="29" y="95" width="10" height="5"/><rect x="69" y="91" width="10" height="5"/><rect x="109" y="89" width="10" height="5"/><rect x="149" y="90" width="10" height="5"/><rect x="189" y="97" width="10" height="5"/></g>
      <g fill="#003a78"><rect x="29" y="65" width="10" height="5"/><rect x="69" y="59" width="10" height="5"/><rect x="109" y="54" width="10" height="5"/><rect x="149" y="66" width="10" height="5"/><rect x="189" y="80" width="10" height="5"/></g>
      <g fill="#fff" text-anchor="middle" font-size="3.3"><text x="34" y="26">63%</text><text x="74" y="45">48%</text><text x="114" y="43">50%</text><text x="154" y="30">60%</text><text x="194" y="18">69%</text><text x="34" y="69">30%</text><text x="74" y="63">42%</text><text x="114" y="58">38%</text><text x="154" y="70">29%</text><text x="194" y="84">18%</text><text x="34" y="99">7%</text><text x="74" y="95">10%</text><text x="114" y="93">12%</text><text x="154" y="94">11%</text><text x="194" y="101">13%</text></g>
      <line x1="50" y1="134" x2="58" y2="134" stroke="#0677BA"/><text x="59" y="135.3" font-weight="700">Ready Unit</text>
      <line x1="86" y1="134" x2="94" y2="134" stroke="#003a78"/><text x="95" y="135.3" font-weight="700">Off Plan</text>
      <line x1="115" y1="134" x2="123" y2="134" stroke="#7BADD7"/><text x="124" y="135.3" font-weight="700">Self Construction</text>
    </svg>
  </div>
  <div class="abs" style="left:253px;top:46px;width:76px">
    <div class="hl-title">Key Highlights</div>
    <div class="note" style="margin-top:5px"><ul>
      <li>Self Construction declined in 2022 due to changes in MHA regulations</li>
      <li style="margin-top:4px">Off Plan and Self Construction make up more than 30% of HSF subsidy production</li>
      <li style="margin-top:4px">Off Plan will continue to grow in accordance with new MHA and NHA project plans</li></ul></div>
  </div>
  <div class="foot"><span>6</span><i class="rule"></i><span>© Copyright 2023 Qimma Home Finance. All Rights Reserved.</span><i class="rule"></i><span class="brand">Qimma Home Finance</span></div>
</section>

<!-- 7 Market share pies -->
<section class="slide c1 r3">
  <div class="frame"></div>
  <div class="title-bar">QHF and NBFI Market Share</div>
  <svg class="abs" style="left:0;top:0" width="356" height="180" viewBox="0 0 356 180" font-size="3.8">
    <text x="73" y="49" text-anchor="middle" font-weight="700" font-size="5">2023 YTD NBFI share of overall</text>
    <text x="73" y="55" text-anchor="middle" font-weight="700" font-size="5">production</text>
    <circle cx="73" cy="110" r="38" fill="#0054AA"/>
    <path d="M73,110 L73,72 A38,38 0 0 0 63.55,73.2 Z" fill="#7BADD7"/>
    <text x="52" y="69" font-weight="700" font-size="3.6">4% - SAR 3B</text>
    <text x="62" y="127" fill="#fff" font-size="3.6">96% - SAR</text>
    <rect x="121" y="102" width="2.5" height="2.5" fill="#0054AA"/><text x="125" y="104.5">Non-NBFI HSF</text><text x="125" y="109">Share</text>
    <rect x="121" y="112" width="2.5" height="2.5" fill="#7BADD7"/><text x="125" y="114.5">NBFI HSF Share</text>
    <text x="222" y="41" text-anchor="middle" font-weight="700" font-size="4.6">2023 YTD QHF share of total NBFI</text>
    <text x="222" y="46.5" text-anchor="middle" font-weight="700" font-size="4.6">production</text>
    <circle cx="210" cy="75" r="24" fill="#0054AA"/>
    <path d="M210,75 L210,51 A24,24 0 1 0 214.5,98.6 Z" fill="#7BADD7"/>
    <text x="212" y="58" font-weight="700" font-size="3.4" fill="#fff">47% - SAR 1.2B</text>
    <text x="162" y="71" font-weight="700" font-size="3.4">53% - SAR 1.4B</text>
    <rect x="248" y="71" width="2.5" height="2.5" fill="#0054AA"/><text x="252" y="73.5">QHF NBFI Share</text>
    <rect x="248" y="78" width="2.5" height="2.5" fill="#7BADD7"/><text x="252" y="80.5">NBFI HSF Share</text>
    <text x="228" y="111" text-anchor="middle" font-weight="700" font-size="4.6">2023 YTD QHF share of overall</text>
    <text x="228" y="116.5" text-anchor="middle" font-weight="700" font-size="4.6">production</text>
    <circle cx="210" cy="147" r="26" fill="#0054AA"/>
    <path d="M210,147 L210,121 A26,26 0 0 0 207.7,121.1 Z" fill="#7BADD7"/>
    <text x="176" y="135" font-weight="700" font-size="3.4">1.4% - SAR...</text>
    <text x="206" y="164" font-weight="700" font-size="3.4" fill="#fff">98.6% - SAR 79B</text>
    <rect x="251" y="135" width="2.5" height="2.5" fill="#0054AA"/><text x="255" y="137.5">Bank and NBFI</text><text x="255" y="142">Market Share</text>
    <rect x="251" y="145" width="2.5" height="2.5" fill="#7BADD7"/><text x="255" y="147.5">QHF Market</text><text x="255" y="152">Share</text>
  </svg>
  <div class="foot"><span>9</span><i class="rule"></i><span>© Copyright 2023 Qimma Home Finance. All Rights Reserved.</span><i class="rule"></i><span class="brand">Qimma Home Finance</span></div>
</section>

<!-- 8 SWOT -->
<section class="slide c2 r3">
  <div class="title-bar">QHF SWOT Analysis</div>
  <svg class="abs" style="left:18px;top:33px" width="320" height="146" viewBox="0 0 320 146" font-size="4">
    <rect x="0" y="0" width="320" height="146" fill="#E8F1F8"/>
    <line x1="0" y1="73" x2="128" y2="73" stroke="#7BADD7" stroke-width=".5"/><line x1="192" y1="73" x2="320" y2="73" stroke="#7BADD7" stroke-width=".5"/>
    <line x1="160" y1="0" x2="160" y2="32" stroke="#7BADD7" stroke-width=".5"/><line x1="160" y1="114" x2="160" y2="146" stroke="#7BADD7" stroke-width=".5"/>
    <path d="M160,33 A40,40 0 0 1 200,73 L190,73 A30,30 0 0 0 160,43 Z" fill="#003a78"/>
    <path d="M200,73 A40,40 0 0 1 160,113 L160,103 A30,30 0 0 0 190,73 Z" fill="#0054AA"/>
    <path d="M160,113 A40,40 0 0 1 120,73 L130,73 A30,30 0 0 0 160,103 Z" fill="#0677BA"/>
    <path d="M120,73 A40,40 0 0 1 160,33 L160,43 A30,30 0 0 0 130,73 Z" fill="#7BADD7"/>
    <circle cx="160" cy="73" r="30" fill="#fff" stroke="#CADEEF" stroke-width="1.5"/>
    <text x="160" y="77" text-anchor="middle" font-size="10" font-weight="800" fill="#003a78">SWOT</text>
    <g fill="#fff" font-weight="700" font-size="6"><text x="145" y="40">01</text><text x="186" y="70">02</text><text x="156" y="110">03</text><text x="123" y="83">04</text></g>
    <g fill="#0054AA" font-weight="700" font-size="6.2"><text x="20" y="8">STRENGTHS</text><text x="261" y="8">WEAKNESSES</text><text x="20" y="141">OPPORTUNITIES</text><text x="270" y="141">THREATS</text></g>
    <circle cx="10" cy="138" r="4" fill="none" stroke="#0054AA" stroke-width=".8"/>
    <path d="M307,141 L312,132 L317,141 Z" fill="none" stroke="#0054AA" stroke-width=".7"/>
    <g font-size="3.7" fill="#333">
      <text x="5" y="19">•&nbsp; Mortgage specialization</text><text x="5" y="27">•&nbsp; Flagship program</text><text x="5" y="35">•&nbsp; NBFI market share</text><text x="5" y="43">•&nbsp; Program management expertise</text><text x="5" y="51">•&nbsp; Mortgage servicing capabilities</text><text x="5" y="59">•&nbsp; Off balance sheet loan book</text>
      <text x="5" y="87">•&nbsp; Grow market share of existing products</text><text x="5" y="95">•&nbsp; Explore new markets</text><text x="5" y="103">•&nbsp; Develop new mortgage products</text><text x="5" y="111">•&nbsp; Digital innovation</text><text x="5" y="119">•&nbsp; Develop new business lines</text>
      <text x="210" y="15">•&nbsp; Mortgage only</text><text x="210" y="23">•&nbsp; Ready-unit only</text><text x="210" y="31">•&nbsp; Flagship program concentration</text><text x="210" y="39">•&nbsp; Geographical reach</text><text x="210" y="47">•&nbsp; Revenue stream dependency</text><text x="210" y="55">•&nbsp; On-balance sheet portfolio size</text>
      <text x="210" y="81">•&nbsp; Subsidy shift</text><text x="210" y="88">•&nbsp; HSF shift</text><text x="210" y="95">•&nbsp; MHS shift</text><text x="210" y="102">•&nbsp; Speed of digital transformation</text><text x="210" y="109">•&nbsp; Regulatory oversight</text><text x="210" y="116">•&nbsp; Competitive pressure from banks</text><text x="210" y="123">•&nbsp; Macro factors (interest rates / property</text><text x="214" y="129">values)</text>
    </g>
  </svg>
  <div class="foot"><span>11</span><i class="rule"></i><span>© Copyright 2023 Qimma Home Finance. All Rights Reserved.</span><i class="rule"></i><span class="brand">Qimma Home Finance</span></div>
</section>

<!-- 9 Competitors -->
<section class="slide c3 r3">
  <div class="frame"></div>
  <div class="title-bar">Competitor Financial Comparison</div>
  <table class="abs comp">
    <tr><th class="lab">H1 2023</th><th class="own">QHF</th><th>Sahel</th><th>Rafid</th><th>Wadi</th><th class="dk">Manzil</th><th>Jisr</th><th class="lt">Tamr</th><th class="lt">Ufuq</th></tr>
    <tr><td>Paid Capital (M)</td><td>359</td><td>900</td><td>575</td><td>1,000</td><td>906</td><td>1,000</td><td>714</td><td>300</td></tr>
    <tr><td>Total Assets (M)</td><td>969</td><td>3,050</td><td>2,324</td><td>4,307</td><td>3,555</td><td>2,085</td><td>1,521</td><td>889</td></tr>
    <tr><td>Shareholder Equity (M)</td><td>589</td><td>892</td><td>700</td><td>1,663</td><td>1,182</td><td>1,342</td><td>882</td><td>366</td></tr>
    <tr><td>Borrowings (M)</td><td>36</td><td>1,705</td><td>1,500</td><td>2,544</td><td>2,031</td><td>669</td><td>595</td><td>405</td></tr>
    <tr><td>Portfolio Size On/Off B/S (M)</td><td>10,080</td><td>2,855</td><td>2,130</td><td>4,076</td><td>3,246</td><td>1,895</td><td>1,019</td><td>725</td></tr>
    <tr><td>Net Income (annualized) (M)</td><td>29.2</td><td class="neg">(48.8)</td><td>2.0</td><td>8.6</td><td>34.6</td><td>107.4</td><td>57.0</td><td>55.8</td></tr>
    <tr><td>ROE (annualized)</td><td>4.9%</td><td class="neg">(5.4%)</td><td>0.2%</td><td>0.6%</td><td>3.0%</td><td>8.0%</td><td>6.5%</td><td>15%</td></tr>
  </table>
  <svg class="abs" style="left:0;top:0" width="356" height="200" viewBox="0 0 356 200" fill="none" stroke="#33475b" stroke-width=".5">
    <path d="M78,142 Q78,150 90,150 L119,150 Q124,150 124,156 Q124,150 129,150 L158,150 Q168,150 168,142"/>
    <path d="M170,142 Q170,150 178,150 L185,150 Q190,150 190,156 Q190,150 195,150 L205,150 Q212,150 212,142"/>
    <path d="M214,142 Q214,150 222,150 L230,150 Q234,150 234,156 Q234,150 238,150 L248,150 Q256,150 256,142"/>
  </svg>
  <div class="tag" style="left:105px;background:var(--blue)">Mainly RF</div>
  <div class="tag" style="left:171px;background:var(--slate)">RF &amp; SME</div>
  <div class="tag" style="left:215px;background:var(--blue-light)">PF &amp; SME</div>
  <div class="abs" style="left:266px;top:52px;width:66px">
    <div class="hl-title">Key Highlights</div>
    <div class="note" style="margin-top:6px"><ul><li>RF competitor's net income impacted in 2023 by high borrowing costs and interest rate mismatch</li><li style="margin-top:5px">Companies who are in the Personal Finance and SME business have the highest ROE</li></ul></div>
  </div>
  <div class="foot"><span>14</span><i class="rule"></i><span>© Copyright 2023 Qimma Home Finance. All Rights Reserved.</span><i class="rule"></i><span class="brand">Qimma Home Finance</span></div>
</section>

<!-- 10 Divider -->
<section class="slide divider c1 r4">
  <i class="abs line-t"></i><i class="abs dot"></i>
  <h2>2.&nbsp; Strategy and Financial Plan</h2>
  <i class="abs line-b"></i>
  <div class="foot"><span>15</span><i class="rule"></i><span>© Copyright 2023 Qimma Home Finance. All Rights Reserved.</span><i class="rule"></i><span class="brand">Qimma Home Finance</span></div>
</section>

<!-- 11 Statement -->
<section class="slide c2 r4">
  <div class="frame"></div>
  <div class="abs statement">Transformation<br>Strategy Statement</div>
  <div class="abs statement-text">
    <p>As we transform into a comprehensive financial services company, we remain committed to continue extending our range and reach of mortgage solutions.</p>
    <p>Our strategy involves expanding our offering beyond mortgages to deliver a broader range of financial solutions to consumers and small and medium enterprises while maintaining our commitment to bespoke experience and technological advancement.</p>
  </div>
  <div class="foot"><span>16</span><i class="rule"></i><span>© Copyright 2023 Qimma Home Finance. All Rights Reserved.</span><i class="rule"></i><span class="brand">Qimma Home Finance</span></div>
</section>

<!-- 12 Current vs future -->
<section class="slide c3 r4">
  <div class="frame"></div>
  <div class="title-bar">Current and Future State Comparison</div>
  <div class="col-head" style="left:63px;color:var(--blue-mid)">Current State</div>
  <div class="col-head" style="left:188px;color:var(--blue-deep)">Future State</div>
  <div class="pill now" style="top:50px">Mortgage originator &amp;<br>service provider</div>
  <div class="pill now" style="top:80px">Single Program Value<br>Proposition</div>
  <div class="pill now" style="top:110px">Limited Geographic<br>Reach</div>
  <div class="pill now" style="top:140px">Single Source of<br>Funding</div>
  <div class="pill next" style="top:48px">Financial Services</div>
  <div class="pill next" style="top:78px">Diverse finance<br>solutions</div>
  <div class="pill next" style="top:108px">Expansive<br>Geographic Reach</div>
  <div class="pill next" style="top:138px">Multiple Sources of<br>Funding</div>
  <div class="foot"><span>17</span><i class="rule"></i><span>© Copyright 2023 Qimma Home Finance. All Rights Reserved.</span><i class="rule"></i><span class="brand">Qimma Home Finance</span></div>
</section>

<!-- 13 KPIs -->
<section class="slide c1 r5">
  <div class="frame"></div>
  <div class="title-bar">Financial Objectives and KPIs</div>
  <div class="kpi-head" style="left:25px;width:148px;background:var(--blue-deep)">Financial KPIs</div>
  <div class="kpi-head" style="left:178px;width:143px;background:var(--blue-mid)">Production and Customer KPIs</div>
  <div class="kpi-cols" style="left:73px"><span style="width:34px">2023</span><span style="width:34px">2026</span><span>Change</span></div>
  <div class="kpi-cols" style="left:228px"><span style="width:32px">2023</span><span style="width:34px">2026</span><span>Change</span></div>

  <div class="kpi-row" style="left:25px;top:78px"><div class="chev" style="width:46px;background:var(--blue-deep)">Portfolio<br>Size</div><div class="chev val" style="width:36px;background:var(--blue-pale)">15.5B</div><div class="chev val" style="width:36px;background:var(--blue-pale)">20.5B</div><div class="chev val strong" style="width:36px;background:var(--blue)">+ 32%</div></div>
  <div class="kpi-row" style="left:25px;top:100px"><div class="chev" style="width:46px;background:var(--blue-deep)">Net<br>Income</div><div class="chev val" style="width:36px;background:var(--blue-pale)">29.3M</div><div class="chev val" style="width:36px;background:var(--blue-pale)">50.3M</div><div class="chev val strong" style="width:36px;background:var(--blue)">+ 72%</div></div>
  <div class="kpi-row" style="left:25px;top:122px"><div class="chev" style="width:46px;background:var(--blue-deep)">ROE</div><div class="chev val" style="width:36px;background:var(--blue-pale)">4.9%</div><div class="chev val" style="width:36px;background:var(--blue-pale)">TBD</div><div class="chev val strong" style="width:36px;background:var(--blue)"></div></div>

  <div class="kpi-row" style="left:178px;top:78px"><div class="chev" style="width:46px;background:var(--blue-mid)">Market<br>Share</div><div class="chev val" style="width:36px;background:var(--blue-mist)">1.7%</div><div class="chev val" style="width:36px;background:var(--blue-mist)">2.1%</div><div class="chev val" style="width:36px;background:var(--blue-light)">+ 24%</div></div>
  <div class="kpi-row" style="left:178px;top:100px"><div class="chev" style="width:46px;background:var(--blue-mid)">HSF Rank</div><div class="chev val" style="width:36px;background:var(--blue-mist)"># 8</div><div class="chev val" style="width:36px;background:var(--blue-mist)"># 7</div><div class="chev val" style="width:36px;background:var(--blue-light)">+ 1</div></div>
  <div class="kpi-row" style="left:178px;top:122px"><div class="chev" style="width:46px;background:var(--blue-mid)">Turnaroun<br>d Time</div><div class="chev val" style="width:36px;background:var(--blue-mist);line-height:1">21<br>days</div><div class="chev val" style="width:36px;background:var(--blue-mist);line-height:1">12<br>days</div><div class="chev val" style="width:36px;background:var(--blue-light)">+ 43%</div></div>
  <div class="abs" style="left:22px;top:168px;font-size:4.6px">*&nbsp; Work in progress. To be finalized prior to Board strategy session.</div>
  <div class="foot"><span>18</span><i class="rule"></i><span>© Copyright 2023 Qimma Home Finance. All Rights Reserved.</span><i class="rule"></i><span class="brand">Qimma Home Finance</span></div>
</section>

<!-- 14 Pillars -->
<section class="slide c2 r5">
  <div class="frame"></div>
  <div class="title-bar">5 QHF Transformation Pillars</div>
  <svg class="abs" style="left:0;top:0" width="356" height="200" viewBox="0 0 356 200">
    <defs><linearGradient id="roof" x1="0" y1="0" x2="0" y2="1"><stop offset="0" stop-color="#E8F1F8"/><stop offset="1" stop-color="#CADEEF"/></linearGradient></defs>
    <path d="M24,66 L170,33 L316,66 Z" fill="url(#roof)"/>
    <rect x="24" y="65" width="292" height="4" fill="#d9d9d9"/>
    <rect x="22" y="158" width="292" height="11" fill="#33475b"/>
    <text x="168" y="165.5" text-anchor="middle" fill="#fff" font-size="5" font-weight="700">QHF Transformation Pillars</text>
  </svg>
  <div class="pillar" style="left:24px;background:#003a78"><svg width="16" height="16" viewBox="0 0 16 16" fill="none" stroke="#fff" stroke-width="1"><path d="M8,14 L2,8 A3.5,3.5 0 0 1 8,3.5 A3.5,3.5 0 0 1 14,8 Z"/></svg><div class="pl">Market<br>Penetration</div></div>
  <div class="pillar" style="left:83px;background:#0054AA"><svg width="16" height="16" viewBox="0 0 16 16" fill="none" stroke="#fff" stroke-width="1"><circle cx="8" cy="8" r="3"/><circle cx="8" cy="8" r="6" stroke-dasharray="2 1.5"/></svg><div class="pl">Product<br>Development</div></div>
  <div class="pillar" style="left:142px;background:#0677BA"><svg width="16" height="16" viewBox="0 0 16 16" fill="none" stroke="#fff" stroke-width="1"><path d="M2,14 V9 M6,14 V6 M10,14 V8 M14,14 V3"/></svg><div class="pl">Market<br>Development</div></div>
  <div class="pillar" style="left:201px;background:#4a92c9"><svg width="16" height="16" viewBox="0 0 16 16" fill="none" stroke="#fff" stroke-width="1"><rect x="3" y="1.5" width="10" height="13"/><path d="M5,5 H11 M5,8 H11 M5,11 H11"/></svg><div class="pl" style="top:47px">Diversification</div></div>
  <div class="pillar" style="left:260px;background:#7BADD7"><svg width="16" height="16" viewBox="0 0 16 16" fill="none" stroke="#fff" stroke-width="1"><circle cx="8" cy="8" r="6"/><circle cx="8" cy="8" r="3"/><path d="M8,8 L14,2"/></svg><div class="pl" style="top:47px">Technology</div></div>
  <div class="foot"><span>19</span><i class="rule"></i><span>© Copyright 2023 Qimma Home Finance. All Rights Reserved.</span><i class="rule"></i><span class="brand">Qimma Home Finance</span></div>
</section>

<!-- 15 Pillar 1 -->
<section class="slide c3 r5">
  <div class="frame"></div>
  <div class="title-bar">Pillar #1: Market Penetration</div>
  <div class="abs impact"><b>+200</b><span>million<br>production<br>impact</span></div>
  <div class="abs" style="left:25px;top:35px;font-size:5.6px;color:#444">Grow market share of residential finance in existing market</div>
  <div class="abs" style="left:25px;top:46px;width:264px;height:11px;background:var(--blue);color:#fff;font-size:6px;font-weight:700;text-align:center;line-height:11px">Market Penetration</div>
  <div class="card" style="left:24px"><h4>Improve<br>Productivity</h4><ul><li>Increase sales productivity across regions</li><li>Clinical focus on volatile and low performers</li><li>Revise incentive scheme</li><li>Seasonal sales Campaigns</li></ul></div>
  <div class="card" style="left:91px"><h4>Increase Leads &amp;<br>conversion</h4><ul><li>Revise leads assignment and utilization criteria</li><li>Continue to challenge and improve QHF marketing activities</li></ul></div>
  <div class="card" style="left:158px"><h4>Increase<br>Sales Head<br>Count</h4><ul><li>Increase HC in existing branches i.e. Capital, Coast, North</li><li>New HC allocated for new branches</li></ul></div>
  <div class="card" style="left:225px"><h4>Implement CRM<br>Platform</h4><ul style="list-style:none;padding-left:4px"><li>Benefits include:</li><li>• Improved customer relationships</li><li>• Enhanced data management</li><li>• Increased efficiency in sales and marketing processes</li></ul></div>
  <div class="foot"><span>20</span><i class="rule"></i><span>© Copyright 2023 Qimma Home Finance. All Rights Reserved.</span><i class="rule"></i><span class="brand">Qimma Home Finance</span></div>
</section>

</body>
</html>
```